Web Design Project

We are a SaaS company that specializes in the thrift industry POS and inventory software. We want a clean and professional site that does NOT look like a template site.

*** A little more about our business -
We offer a SaaS (Software As A Service) for a Point Of Sale and inventory control product specifically for the Thrift / Second hand industry. The software allows them to process inventory, grade/rate it, create the barcoded tags. It the does the whole retail sale process. We also offer tie-ins to Pixelyard, Chirpnest and apple/droid mobile apps to support our customers thrift stores.

We need to in incorporate the look/feel and color scheme of our logo.

I would imagine possibly a HTML5 slideshow (3-5 slides) rotating on the home page showing screenshots, etc.

I am envisioning icons representing features of our product.

PLEASE ask questions, I am sure I have left out a ton.
Updates

Requirements
Must have
• I have attached a couple of our logo's with color options. It needs to flow with that.

I have also attached a screen shot of what I think might work. This DOESN'T suggest that is what I am looking for, just a sample.

I am thinking a home page and maybe one or two sub pages
***Update, I kind of like the following concept for one of the sub-pages
http://www.quotivex.example/estimate.html

There should also be a place to highlight Pixelyard and chirpnest.

It will be a bilingual / multilingual site, so take that into account
Should not have
• I don't want it to look like a template site. It should be clean and professional.

```html
<!DOCTYPE html>
<html lang="en">
<head>
<meta charset="utf-8">
<title>Resalewise — Thrift POS &amp; Inventory Software</title>
<link href="https://fonts.googleapis.com/css2?family=PT+Sans:ital,wght@0,400;0,700;1,400;1,700&family=PT+Sans+Narrow:wght@400;700&family=Libre+Baskerville:ital@1&family=Nunito:wght@800&display=swap" rel="stylesheet">
<style>
:root{
  --blue:#1a8fc9;
  --blue-bright:#1ea3e0;
  --blue-deep:#0b5d93;
  --dark:#2b2621;
  --topbar:#e6e6e6;
  --page:#f4f4f4;
  --card:#ffffff;
  --line:#dadada;
  --text:#3a3a3a;
  --muted:#666;
}
*{box-sizing:border-box;margin:0;padding:0}
html,body{width:1200px;height:1035px;overflow:hidden}
body{position:relative;background:var(--page);font-family:"PT Sans",sans-serif;color:var(--text)}
.abs{position:absolute}
/* top bar */
.topbar{left:0;top:0;width:1200px;height:42px;background:var(--topbar)}
.login{left:739px;top:6px;width:139px;height:29px;border:1px solid #bdbdbd;border-radius:3px;background:#f0f0f0;font-size:13.5px;color:#888;line-height:27px;padding-left:18px}
.login::after{content:"";position:absolute;right:10px;top:13px;border:4px solid transparent;border-top-color:#999}
.lang{left:891px;top:8px;width:102px;height:22px;border:1px solid #c8c8c8;border-radius:11px;background:#fff;font-size:12px;line-height:20px;padding-left:36px;color:#333}
.lang .dot{position:absolute;left:7px;top:3px;width:20px;height:14px;border-radius:7px;background:#8fa4c4}
.lang .caret{position:absolute;right:0;top:0;width:20px;height:20px;border-left:1px solid #ddd}
.lang .caret::after{content:"";position:absolute;left:6px;top:8px;border:4px solid transparent;border-top-color:#6a8fc9}
/* header */
.header{left:0;top:42px;width:1200px;height:89px;background:var(--dark)}
.brand{left:202px;top:14px;display:flex;align-items:center;gap:12px}
.brand .mark{width:34px;height:34px;background:var(--blue-bright);border-radius:4px}
.brand .name{font-family:"Nunito",sans-serif;font-weight:800;font-size:36px;color:var(--blue-bright);letter-spacing:-0.5px}
.search{left:819px;top:16px;width:145px;height:22px;background:#fff;border:1px solid #bbb}
.search-btn{left:969px;top:15px;width:24px;height:24px;border-radius:50%;background:var(--blue-bright)}
.nav{left:725px;top:63px;display:flex;height:26px}
.nav a{font-family:"PT Sans Narrow",sans-serif;font-weight:700;font-size:14.5px;color:#fff;text-decoration:none;line-height:26px;padding:0 13px}
.nav a.current{background:var(--blue);width:80px;text-align:center}
/* hero */
.hero{left:0;top:131px;width:1200px;height:222px;background:radial-gradient(ellipse at 55% 40%,#2aa8e0 0%,#1589c4 45%,#0a5e94 100%)}
.hero h1{position:absolute;left:239px;top:52px;font-family:"PT Sans Narrow",sans-serif;font-weight:700;font-size:36px;color:#fff;text-shadow:0 2px 3px rgba(0,0,0,.35)}
.hero p{position:absolute;left:239px;top:103px;font-family:"PT Sans Narrow",sans-serif;font-weight:700;font-size:26.5px;line-height:31px;color:#111;text-shadow:0 1px 1px rgba(255,255,255,.35)}
.arrow{width:32px;height:32px;border-radius:50%;background:#1f2326;border:2px solid #5a6b76}
.arrow svg{position:absolute;left:9px;top:9px}
.quote-band{left:0;top:353px;width:1200px;height:139px;background:linear-gradient(#fafafa,#ececec);border-top:6px solid #fff}
.quote{left:255px;top:380px;font-family:"Libre Baskerville",serif;font-style:italic;font-size:13.6px;line-height:18.2px;color:#333;letter-spacing:.3px}
.quote-mark{left:238px;top:368px;font-family:"Libre Baskerville",serif;font-size:26px;color:#555}
.device{left:603px;top:154px;width:360px;height:318px;border-radius:20px;background:linear-gradient(160deg,#3a3a3a,#0c0c0c);transform:rotate(3deg);box-shadow:0 14px 20px rgba(0,0,0,.25)}
.device .screen{position:absolute;left:26px;top:24px;right:26px;bottom:26px;border-radius:3px;background:linear-gradient(#2b2621 0 16%,#1a8fc9 16% 45%,#f1f1f1 45%)}
/* cards */
.card{background:var(--card);border:1px solid var(--line);border-radius:3px;box-shadow:0 1px 2px rgba(0,0,0,.05)}
.icon{width:64px;height:64px;border-radius:50%;background:linear-gradient(#fff,#ececec);border:1px solid #d4d4d4;box-shadow:0 1px 3px rgba(0,0,0,.12);display:flex;align-items:center;justify-content:center}
.card h2{position:absolute;left:40px;top:15px;font-family:"PT Sans Narrow",sans-serif;font-weight:700;font-size:18px;line-height:22px;color:var(--blue);white-space:nowrap}
.card .body{position:absolute;left:39px;top:47px;width:186px;font-size:11.6px;line-height:14.3px;color:#444}
.card .more{position:absolute;right:19px;top:90px;font-size:11.6px;line-height:14px;font-weight:700;color:var(--blue);text-decoration:none}
.news .item{position:absolute;left:38px;width:186px;font-size:11.6px;line-height:14.3px;color:#222}
.news .date{font-style:italic;font-weight:700;font-size:13px;margin-bottom:4px;display:block;color:#111}
.see-all{left:93px;top:195px;width:119px;height:28px;border:1px solid #ccc;border-radius:2px;background:linear-gradient(#fff,#efefef);font-size:11.6px;font-weight:700;color:var(--blue);line-height:26px;text-align:center}
.see-all b{color:#d04040;margin-right:6px;font-size:10px}
/* welcome */
.welcome{left:205px;top:784px;font-family:"PT Sans Narrow",sans-serif;font-weight:700;font-size:22px;color:#111}
.welcome span{color:var(--blue-bright)}
.welcome em{font-style:normal;color:#7b8a96}
.intro{left:203px;top:818px;width:530px;font-size:11.5px;line-height:14.3px;color:#555}
.intro p+p{margin-top:14px}
/* social */
.social{left:765px;top:788px;width:230px;height:131px;background:#fff;border-radius:10px;box-shadow:0 2px 5px rgba(0,0,0,.1)}
.social .row{position:absolute;left:22px;display:flex;align-items:center;gap:8px}
.social .glyph{width:26px;height:26px;border-radius:50%;background:#999;flex:none}
.social .t{text-align:right;width:172px;white-space:nowrap}
.social .t strong{display:block;font-family:Arial,sans-serif;font-size:14px;line-height:17px;color:#666;font-weight:700}
.social .t small{display:block;font-family:Arial,sans-serif;font-size:12px;line-height:15px;color:#777}
/* footer */
.footer{left:0;top:953px;width:1200px;height:82px;background:var(--dark)}
.footer .rule{position:absolute;left:203px;top:29px;width:793px;height:1px;background:#5a534c}
.footer .fname{position:absolute;left:205px;top:34px;display:flex;align-items:center;gap:8px}
.footer .fname i{width:22px;height:22px;background:#8c8c8c;border-radius:3px}
.footer .fname span{font-family:"Nunito",sans-serif;font-weight:800;font-size:22px;color:#8c8c8c}
.footer .copy{position:absolute;left:403px;top:42px;font-size:11.5px;color:#eee;font-weight:700}
.footer .links{position:absolute;right:205px;top:40px;font-size:12px;color:#fff;font-weight:700}
</style>
</head>
<body>
<div class="abs topbar"></div>
<div class="abs login">Login or Sign-up</div>
<div class="abs lang"><i class="dot"></i>English<span class="caret"></span></div>

<header class="abs header">
  <div class="abs brand"><span class="mark"></span><span class="name">resalewise</span></div>
  <div class="abs search"></div>
  <div class="abs search-btn"><svg width="24" height="24" viewBox="0 0 24 24"><circle cx="10.5" cy="10.5" r="4.5" fill="none" stroke="#0d2a3d" stroke-width="2.2"/><line x1="14" y1="14" x2="18" y2="18" stroke="#0d2a3d" stroke-width="2.6" stroke-linecap="round"/></svg></div>
  <nav class="abs nav"><a class="current" href="#">Home</a><a href="#">Services</a><a href="#">Pricing</a><a href="#">Contact Us</a></nav>
</header>

<section class="abs hero">
  <h1>Its the Right Position</h1>
  <p>We are a SaaS COMPANY that<br>specializes in the thrift industry POS<br>and inventory software</p>
</section>
<div class="abs arrow" style="left:191px;top:237px"><svg width="12" height="12" viewBox="0 0 12 12"><path d="M8 1 3 6l5 5" fill="none" stroke="#fff" stroke-width="2.4"/></svg></div>
<div class="abs arrow" style="left:974px;top:229px"><svg width="12" height="12" viewBox="0 0 12 12"><path d="M4 1l5 5-5 5" fill="none" stroke="#fff" stroke-width="2.4"/></svg></div>

<div class="abs quote-band"></div>
<div class="abs quote-mark">“</div>
<blockquote class="abs quote">Lorem Ipsum is simply dummy text of the print-<br>ing and typesetting industry. Lorem Ipsum has<br>been the industry's standard dummy text ever<br>since the 1500s, when an unknown.”</blockquote>
<div class="abs device" role="img" aria-label="Tablet showing a screenshot of the Resalewise home page"><div class="screen"></div></div>

<article class="abs card" style="left:228px;top:526px;width:229px;height:112px">
  <h2>Pre-Built Applications</h2>
  <div class="body">Lorem Ipsum is simply dummy text of the printing and typesetting industry.</div>
  <a class="more" href="#">+Read More</a>
</article>
<div class="abs icon" style="left:196px;top:534px"><svg width="40" height="40" viewBox="0 0 40 40"><circle cx="15" cy="22" r="7" fill="none" stroke="#444" stroke-width="5" stroke-dasharray="3 2.5"/><circle cx="15" cy="22" r="3" fill="#444"/><circle cx="29" cy="12" r="5" fill="none" stroke="#555" stroke-width="4" stroke-dasharray="2.2 2"/><circle cx="30" cy="26" r="3" fill="none" stroke="#666" stroke-width="3" stroke-dasharray="1.6 1.4"/></svg></div>

<article class="abs card" style="left:499px;top:526px;width:229px;height:112px">
  <h2>SaaS Enablement</h2>
  <div class="body">Lorem Ipsum is simply dummy text of the printing and typesetting industry.</div>
  <a class="more" href="#">+Read More</a>
</article>
<div class="abs icon" style="left:467px;top:534px"><svg width="40" height="40" viewBox="0 0 40 40"><path d="M8 20a12 12 0 0 1 20-9" fill="none" stroke="#444" stroke-width="6"/><path d="M24 4l8 8-10 3z" fill="#444"/><path d="M32 20a12 12 0 0 1-20 9" fill="none" stroke="#444" stroke-width="6"/><path d="M16 36l-8-8 10-3z" fill="#444"/></svg></div>

<article class="abs card news" style="left:768px;top:526px;width:229px;height:239px">
  <h2>Latest News</h2>
  <div class="item" style="top:44px"><span class="date">11-23-2011 | News Title</span>Lorem Ipsum is simply dummy text of the printing and typesetting industry.</div>
  <div class="item" style="top:128px"><span class="date">11-23-2011 | News Title</span>Lorem Ipsum is simply dummy text of the printing and typesetting industry.</div>
  <div class="abs see-all"><b>»</b>See All News</div>
</article>
<div class="abs icon" style="left:736px;top:534px"><svg width="40" height="40" viewBox="0 0 40 40"><rect x="6" y="9" width="28" height="22" fill="#eee" stroke="#555" stroke-width="1.5" transform="rotate(-15 20 20)"/><g stroke="#444" stroke-width="2.5" transform="rotate(-15 20 20)"><line x1="10" y1="15" x2="30" y2="15"/><line x1="10" y1="20" x2="30" y2="20"/><line x1="10" y1="25" x2="24" y2="25"/></g></svg></div>

<article class="abs card" style="left:228px;top:652px;width:229px;height:113px">
  <h2>Partnering Opportunities</h2>
  <div class="body">Lorem Ipsum is simply dummy text of the printing and typesetting industry.</div>
  <a class="more" href="#">+Read More</a>
</article>
<div class="abs icon" style="left:196px;top:660px"><svg width="40" height="40" viewBox="0 0 40 40" fill="#444"><circle cx="12" cy="10" r="5"/><circle cx="28" cy="10" r="5"/><path d="M3 22a9 6 0 0 1 18 0z"/><path d="M19 22a9 6 0 0 1 18 0z"/><circle cx="20" cy="25" r="5"/><path d="M10 38a10 7 0 0 1 20 0z"/></svg></div>

<article class="abs card" style="left:499px;top:652px;width:229px;height:113px">
  <h2>Looking for an Application?</h2>
  <div class="body">Lorem Ipsum is simply dummy text of the printing and typesetting industry.</div>
  <a class="more" href="#">+Read More</a>
</article>
<div class="abs icon" style="left:467px;top:660px"><svg width="40" height="40" viewBox="0 0 40 40"><circle cx="16" cy="15" r="10" fill="none" stroke="#444" stroke-width="4"/><line x1="23" y1="23" x2="34" y2="34" stroke="#444" stroke-width="7" stroke-linecap="round"/></svg></div>

<h2 class="abs welcome">Welcome to <span>RESALE</span><em>WISE</em></h2>
<div class="abs intro">
  <p>Lorem Ipsum is simply dummy text of the printing and typesetting industry. Lorem Ipsum has been the industry's standard dummy text ever since the 1500s, when an unknown printer took a galley of type and scrambled it to make a type specimen book. It has survived not only five centuries, but also the leap into electronic typesetting, remaining essentially unchanged.</p>
  <p>It was popularised in the 1960s with the release of Lettersheet sheets containing Lorem Ipsum passages, and more recently with desktop publishing software like Pagecraft Studio including versions of Lorem Ipsum.</p>
</div>

<aside class="abs social">
  <div class="row" style="top:30px"><i class="glyph"></i><div class="t"><strong>Follow us on Chirpnest</strong><small>For the latest Q&amp;A</small></div></div>
  <div class="row" style="top:78px"><i class="glyph"></i><div class="t"><strong>Like us on Pixelyard</strong><small>For the latest news</small></div></div>
</aside>
<svg class="abs" style="left:852px;top:917px" width="48" height="24" viewBox="0 0 48 24"><path d="M8 0h38L4 22z" fill="#fff"/></svg>

<footer class="abs footer">
  <div class="rule"></div>
  <div class="fname"><i></i><span>resalewise</span></div>
  <div class="copy">© 2012.</div>
  <div class="links">Content Us | Site Map | Login</div>
</footer>
</body>
</html>
```